New Website for NY and South Florida Based Accounting Firm

Accounting and Audit firm located in New York and South Florida needs a website redesign after acquiring new businesses and adding new services.

Our current website can be found here:
http://www.trqbnllp.example/

We have merged with this firm:
http://hollisbarkerwendtfield.example/

We are looking for a comprehensive design that will highlight the firm's dual locations. The final design should communicate security, strength, and growth. We would like to keep our pyramid logo as seen on the trqbnllp.example website, as this has been our logo for over 20 years.

Industry/Entity Type

Accounting

Number of Pages Required

1 page

Font styles to use
Serif
Sans Serif

```html
<!DOCTYPE html>
<html lang="en">
<head>
<meta charset="utf-8">
<title>Thornbury, Renwick, Quill &amp; Bastian, LLP</title>
<link rel="stylesheet" href="https://fonts.googleapis.com/css2?family=Lato:wght@300;400;700&family=Raleway:wght@300;400&display=swap">
<style>
:root{
  --blue:#0b679f;
  --blue-dark:#0a3350;
  --nav:#3a3a3a;
  --ink:#222;
  --grey-band:#5b5b5b;
  --footer:#3e3e3e;
  --muted:#d6d6d6;
  --btn:#7a7a7a;
}
*{margin:0;padding:0;box-sizing:border-box}
html,body{width:683px;height:1200px;overflow:hidden}
body{font-family:'Lato',sans-serif;color:var(--ink);background:#fff;position:relative}
.abs{position:absolute}
.topline{top:0;left:0;width:683px;height:3px;background:#2a2a2a}
.header{top:3px;left:0;width:683px;height:46px;background:var(--blue);color:#fff}
.brand{left:55px;top:13px;font-size:15px;font-variant:small-caps;letter-spacing:.3px;font-weight:400}
.callus{right:55px;top:16px;font-size:11px}
.callus b{font-weight:700}
.nav{top:49px;left:0;width:683px;height:24px;background:var(--nav);border-bottom:1px solid #555}
.nav ul{list-style:none;display:flex;position:absolute;left:55px;top:7px;gap:0}
.nav li{color:#fff;font-size:8.2px;text-transform:uppercase;margin-right:21px}
.login{right:55px;top:5px;background:#ccc;color:#333;font-size:8px;font-weight:700;padding:3px 5px}
.hero{top:73px;left:0;width:683px;height:300px;background:linear-gradient(120deg,#5c6f86 0%,#a7b6c8 40%,#7d8ea5 70%,#c4ccd6 100%)}
.caption{top:324px;left:0;width:683px;height:49px;background:rgba(40,44,52,.75);color:#fff;text-align:center;font-family:'Raleway',sans-serif;font-size:14px;line-height:18px;padding-top:6px}
.section-title{width:683px;text-align:center;font-family:'Raleway',sans-serif;font-size:18px;font-weight:400}
.rule{height:1px;left:158px;width:368px}
.about-text{top:440px;left:95px;width:493px;text-align:center;font-size:7.7px;line-height:14px}
.btn-more{top:506px;left:294px;width:95px;height:24px;background:var(--btn);color:#fff;font-size:8.5px;font-weight:700;text-align:center;line-height:24px}
.services{top:558px;left:0;width:683px;height:290px;background:var(--grey-band);color:#fff}
.video{top:633px;left:56px;width:300px;height:188px;border:1px solid #ccc;background:linear-gradient(180deg,#4a4a4a,#9a9ea3 45%,#7d7f82);}
.vbar{top:800px;left:57px;width:298px;height:20px;background:#111}
.list{top:630px;left:389px;color:var(--muted)}
.list h3{font-family:'Raleway',sans-serif;font-weight:400;font-size:11px;margin-bottom:4px;color:#e6e6e6}
.list ul{padding-left:14px;font-size:7.8px;line-height:15px}
.news{top:848px;left:0;width:683px;height:159px;background:var(--blue);color:#fff}
.news-text{top:922px;left:110px;width:463px;text-align:center;font-size:7.8px;line-height:14px;color:#fff}
.email{top:955px;left:170px;width:242px;height:23px;background:#fff;font-size:6.5px;color:#999;padding:8px 7px}
.subscribe{top:955px;left:418px;width:96px;height:23px;background:var(--blue-dark);color:#fff;font-size:8.5px;font-weight:700;text-align:center;line-height:23px;letter-spacing:.5px}
.footer{top:1007px;left:0;width:683px;height:168px;background:var(--footer);color:#fff}
.fcol h4{font-family:'Raleway',sans-serif;font-weight:400;font-size:10px;padding-bottom:3px;border-bottom:1px solid #bbb;margin-bottom:6px}
.fcol ul{list-style:none;font-size:6.5px;line-height:13px}
.fcol li::before{content:"› ";color:#aaa}
.loc{font-size:6.5px;line-height:8.5px}
.loc b{display:block;font-size:7px;margin-bottom:3px}
.loc p{padding-left:14px;position:relative;margin-bottom:8px}
.loc svg{position:absolute;left:0;top:0}
.contact{font-size:6.5px}
.contact div{height:22.5px;display:flex;gap:8px;align-items:flex-start}
.bottom{top:1175px;left:0;width:683px;height:25px;background:var(--blue);color:#fff;font-size:7px;text-align:center;line-height:25px}
</style>
</head>
<body>
<div class="abs topline"></div>
<header class="abs header">
  <div class="abs brand">Thornbury, Renwick, Quill &amp; Bastian, LLP</div>
  <div class="abs callus"><b>Call Us</b> 555-210-4400</div>
</header>
<nav class="abs nav">
  <ul><li>Home</li><li>Why TRQB? ▾</li><li>Services ▾</li><li>Profiles</li><li>Tips &amp; Links</li><li>Partners</li><li>Resources</li><li>Contact</li></ul>
  <div class="abs login">CLIENT LOGIN</div>
</nav>
<div class="abs hero" role="img" aria-label="Financial photo: calculator, stock chart and stacked coins in blue tones"></div>
<svg class="abs" style="top:193px;left:24px" width="18" height="60"><path d="M16 2 L2 30 L16 58" stroke="#fff" fill="none" stroke-width="1.2"/></svg>
<svg class="abs" style="top:193px;left:641px" width="18" height="60"><path d="M2 2 L16 30 L2 58" stroke="#fff" fill="none" stroke-width="1.2"/></svg>
<div class="abs caption">We use our vast array of resources, depth of knowledge and experience to position<br>you for success, stability and prosperity.</div>

<section>
  <svg class="abs" style="top:399px;left:270px" width="23" height="20" viewBox="0 0 23 20"><rect x="4" y="2" width="15" height="18" fill="#111"/><rect x="0" y="8" width="4" height="12" fill="#111"/><rect x="19" y="8" width="4" height="12" fill="#111"/><g fill="#fff"><rect x="7" y="5" width="2" height="2"/><rect x="11" y="5" width="2" height="2"/><rect x="15" y="5" width="2" height="2"/><rect x="7" y="10" width="2" height="2"/><rect x="11" y="10" width="2" height="2"/><rect x="15" y="10" width="2" height="2"/><rect x="10" y="15" width="3" height="5"/></g></svg>
  <h2 class="abs section-title" style="top:398px;left:26px">About TRQB</h2>
  <div class="abs rule" style="top:428px;background:#ccc"></div>
  <p class="abs about-text">Thornbury, Renwick, Quill &amp; Bastian, LLP is an accounting, audit and business management firm with offices in New York City, Long Island, and Florida. Our experienced CPA's offer financial solutions and vast resources in all aspects of accounting, tax planning, tax return preparation, personal financial planning, estate and trust, and small business consulting. Our services are backed by a commitment to one-on-one attention and an unwavering dedication to meeting the highest business standards.</p>
  <div class="abs btn-more">READ MORE</div>
</section>

<section class="abs services">
  <svg class="abs" style="top:27px;left:249px" width="22" height="20" viewBox="0 0 22 20" fill="#fff"><circle cx="8" cy="11" r="6"/><circle cx="8" cy="11" r="2.5" fill="#5b5b5b"/><circle cx="17" cy="5" r="4"/><circle cx="17" cy="5" r="1.5" fill="#5b5b5b"/><circle cx="17" cy="16" r="3"/></svg>
  <h2 class="abs section-title" style="top:26px;left:30px;color:#fff">Services Overview</h2>
  <div class="abs rule" style="top:59px;left:150px;width:383px;background:#999"></div>
</section>
<div class="abs video" role="img" aria-label="Video still: businessman holding a briefcase against a city skyline"></div>
<svg class="abs" style="top:708px;left:193px" width="26" height="26"><circle cx="13" cy="13" r="12" fill="rgba(255,255,255,.75)"/><path d="M10 7 L19 13 L10 19Z" fill="#555"/></svg>
<div class="abs vbar"></div>
<svg class="abs" style="top:805px;left:62px" width="290" height="10"><path d="M1 1 L8 5 L1 9Z" fill="#fff"/><rect x="12" y="1" width="2.5" height="8" fill="#fff"/><rect x="17" y="1" width="2.5" height="8" fill="#fff"/><rect x="27" y="4" width="260" height="2" fill="#888"/><rect x="27" y="4" width="110" height="2" fill="#c21"/></svg>
<div class="abs list">
  <h3>Lorem ipsum dolor sit amet quem primis</h3>
  <ul>
    <li>Condominium, Homeowner and Timeshare Association</li>
    <li>Services/Auditor</li>
    <li>Audit, Review, and Attestation Services</li>
    <li>Accounting and Tax Services</li>
    <li>Non Profit Audits/Auditors</li>
    <li>Grant Audits/Auditors</li>
    <li>Single and OMB 133 Audits/Auditors</li>
    <li>401-K Audits/Auditors</li>
    <li>Bookkeeping (Compliance Services)</li>
    <li>Financial Planning</li>
    <li>Management Consulting</li>
    <li>Tax Services</li>
  </ul>
</div>

<section class="abs news">
  <svg class="abs" style="top:27px;left:251px" width="20" height="20" viewBox="0 0 20 20" fill="none" stroke="#fff" stroke-width="1.3"><path d="M2 6 L18 2 L14 18 L9 11 Z"/><path d="M9 11 L18 2"/><path d="M1 12h5M2 15h4"/></svg>
  <h2 class="abs section-title" style="top:26px;left:30px;color:#fff">Newsletter Signup</h2>
  <div class="abs rule" style="top:57px;left:150px;width:383px;background:#5c98c2"></div>
</section>
<p class="abs news-text">Lorem ipsum dolor sit amet, consectetuer adipiscing elit, sed diam nonummy nibh euismod tincidunt ut laoreet dolore magna aliquam erat volutpat. Ut wisi enim ad minim veniam.</p>
<div class="abs email">Enter your email address</div>
<div class="abs subscribe">SUBSCRIBE</div>

<footer class="abs footer">
  <div class="abs fcol" style="top:23px;left:56px;width:57px">
    <h4>Quick Links</h4>
    <ul><li>Home</li><li>Why TRQB?</li><li>Services</li><li>Profiles</li><li>Tips &amp; Links</li><li>Partners</li><li>Resources</li><li>Contact Us</li></ul>
  </div>
  <div class="abs fcol" style="top:23px;left:171px;width:139px">
    <h4>Member</h4>
    <ul style="line-height:13.6px"><li>LedgerCircle</li><li>National Guild of Accountants</li><li>Empire State Accountants Forum</li><li>Guild Personal Planning Council</li></ul>
    <h4 style="margin-top:12px">Follow Us On</h4>
    <div style="display:flex;align-items:center;gap:9px;font-size:7.5px;margin-top:2px"><span style="display:block;width:14px;height:14px;background:#fff"></span>Connect On ProNet</div>
  </div>
  <div class="abs fcol" style="top:23px;left:373px;width:125px">
    <h4>Our Locations</h4>
    <div class="loc">
      <b>New York Office</b>
      <p><svg width="6" height="9" viewBox="0 0 6 9"><path d="M3 9 L0 4 A3 3 0 1 1 6 4Z" fill="#fff"/><circle cx="3" cy="3" r="1" fill="#3e3e3e"/></svg>820 Harbor Street<br>2nd Floor New York, NY 10001</p>
      <b>Long Island Office</b>
      <p><svg width="6" height="9" viewBox="0 0 6 9"><path d="M3 9 L0 4 A3 3 0 1 1 6 4Z" fill="#fff"/><circle cx="3" cy="3" r="1" fill="#3e3e3e"/></svg>47 Linden Lane<br>Melville, NY 11700</p>
      <b>Florida Office</b>
      <p><svg width="6" height="9" viewBox="0 0 6 9"><path d="M3 9 L0 4 A3 3 0 1 1 6 4Z" fill="#fff"/><circle cx="3" cy="3" r="1" fill="#3e3e3e"/></svg>300 Coral Way, Suite 12<br>Fort Lauderdale, FL 33300</p>
    </div>
  </div>
  <div class="abs fcol" style="top:23px;left:549px;width:78px">
    <h4>Contact Details</h4>
    <div class="contact">
      <div><svg width="8" height="8" viewBox="0 0 8 8"><path d="M1 0 L3 0 L3.5 2 L2.5 3 Q3.5 5 5 5.5 L6 4.5 L8 5 L8 7 Q4 8 1 4 Q0 2 1 0Z" fill="#fff"/></svg>555-210-4400</div>
      <div><svg width="8" height="8" viewBox="0 0 8 8"><path d="M1 0 L3 0 L3.5 2 L2.5 3 Q3.5 5 5 5.5 L6 4.5 L8 5 L8 7 Q4 8 1 4 Q0 2 1 0Z" fill="#fff"/></svg>555-318-7720</div>
      <div><svg width="8" height="8" viewBox="0 0 8 8" fill="#fff"><rect x="2" y="0" width="4" height="2"/><rect x="0" y="2.5" width="8" height="3.5"/><rect x="2" y="6" width="4" height="2"/></svg>555-210-4401</div>
      <div><svg width="8" height="8" viewBox="0 0 8 8" fill="#fff"><rect x="2" y="0" width="4" height="2"/><rect x="0" y="2.5" width="8" height="3.5"/><rect x="2" y="6" width="4" height="2"/></svg>555-318-7721</div>
      <div><svg width="8" height="7" viewBox="0 0 8 7"><rect x="0" y="1" width="8" height="5.5" fill="#fff"/><path d="M0 1 L4 4 L8 1" stroke="#3e3e3e" fill="none" stroke-width=".8"/></svg>info@trqbnllp.example</div>
    </div>
  </div>
</footer>
<div class="abs bottom">© 2016 THORNBURY, RENWICK, QUILL &amp; BASTIAN, LLP</div>
</body>
</html>
```